VELMARA IMAGING
Ultrasound Imaging Services
VELMARA IMAGING - Imaging
Creative Brief
Professional
Dorvan Tessliff
Ultrasound Diagnostic
5873 Calloway ridge ln Raleigh, NC 27614
dorvantessliff@mailvane.net
Concepts
Logo for mobile ultrasound

```html
<!DOCTYPE html>
<html lang="en">
<head>
<meta charset="utf-8">
<title>Velmara Imaging – Business Card</title>
<link rel="stylesheet" href="https://fonts.googleapis.com/css2?family=Montserrat:wght@400;500;600;700;800&display=swap">
<style>
  :root {
    --bg: #d9dadc;
    --card: #ffffff;
    --navy: #1e1c6e;
    --sky: #3fa9d8;
    --sky-soft: #9fd4ee;
    --ink: #1e1c6e;
    --muted: #5a5f7a;
  }
  html, body {
    margin: 0;
    width: 1200px;
    height: 901px;
    overflow: hidden;
    background: var(--bg);
    font-family: "Montserrat", sans-serif;
  }
  .business-card {
    position: absolute;
    left: 100px;
    top: 164px;
    width: 1000px;
    height: 572px;
    background: var(--card);
    box-shadow: 0 18px 40px rgba(0,0,0,0.18);
    overflow: hidden;
  }
  .card-swoosh {
    position: absolute;
    inset: 0;
  }
  .corner-tab {
    position: absolute;
    top: 0;
    right: 70px;
    width: 60px;
    height: 22px;
    background: var(--navy);
  }
  .brand {
    position: absolute;
    left: 60px;
    top: 220px;
  }
  .brand-row {
    display: flex;
    align-items: center;
    gap: 14px;
  }
  .brand-dot {
    width: 40px;
    height: 40px;
    border-radius: 50%;
    background: var(--sky);
  }
  .brand-name {
    font-weight: 800;
    font-size: 64px;
    letter-spacing: 2px;
    color: var(--navy);
    line-height: 1;
  }
  .brand-services {
    margin: 8px 0 0 54px;
    font-weight: 700;
    font-size: 17px;
    letter-spacing: 1px;
    color: var(--sky);
  }
  .brand-tagline {
    margin: 4px 0 0 54px;
    font-weight: 500;
    font-size: 11px;
    letter-spacing: 2px;
    color: var(--muted);
  }
  .person {
    position: absolute;
    right: 70px;
    top: 60px;
    text-align: right;
  }
  .person-name {
    font-weight: 600;
    font-size: 26px;
    letter-spacing: 2px;
    color: var(--navy);
  }
  .person-role {
    font-size: 15px;
    color: var(--muted);
    margin-top: 4px;
  }
  .contact-list {
    position: absolute;
    right: 70px;
    top: 150px;
    list-style: none;
    margin: 0;
    padding: 0;
    font-size: 15px;
    color: var(--ink);
  }
  .contact-list li {
    display: flex;
    justify-content: flex-end;
    align-items: center;
    gap: 12px;
    height: 30px;
  }
  .contact-icon {
    width: 16px;
    height: 16px;
    fill: var(--navy);
  }
  .address {
    position: absolute;
    left: 60px;
    bottom: 40px;
    color: #ffffff;
    font-size: 17px;
    font-weight: 500;
    line-height: 1.5;
  }
</style>
</head>
<body>
  <article class="business-card">
    <svg class="card-swoosh" viewBox="0 0 1000 572" preserveAspectRatio="none" aria-hidden="true">
      <path d="M0 440 C 300 470, 650 430, 1000 250 L1000 300 C 700 460, 340 500, 0 470 Z" fill="var(--sky-soft)"/>
      <path d="M0 455 C 320 480, 660 440, 1000 280 L1000 330 C 700 480, 340 510, 0 490 Z" fill="var(--sky)"/>
      <path d="M0 470 C 330 500, 680 460, 1000 320 L1000 572 L0 572 Z" fill="var(--navy)"/>
    </svg>
    <div class="corner-tab"></div>

    <div class="brand">
      <div class="brand-row">
        <span class="brand-dot"></span>
        <span class="brand-name">VELMARA</span>
      </div>
      <div class="brand-services">IMAGING ULTRASOUND SERVICES</div>
      <div class="brand-tagline">ACCURATE FAST RESULTS</div>
    </div>

    <div class="person">
      <div class="person-name">DORVAN TESSLIFF</div>
      <div class="person-role">Managing Director</div>
    </div>

    <ul class="contact-list">
      <li>010 482 3061
        <svg class="contact-icon" viewBox="0 0 16 16"><path d="M3 1h3l1 4-2 1a9 9 0 0 0 5 5l1-2 4 1v3a2 2 0 0 1-2 2A13 13 0 0 1 1 3a2 2 0 0 1 2-2z"/></svg>
      </li>
      <li>010 482 3075
        <svg class="contact-icon" viewBox="0 0 16 16"><rect x="4" y="1" width="8" height="14" rx="1.5"/></svg>
      </li>
      <li>dorvantessliff@mailvane.net
        <svg class="contact-icon" viewBox="0 0 16 16"><path d="M1 3h14v10H1z M1 3l7 6 7-6" stroke="#fff" stroke-width="1"/></svg>
      </li>
      <li>www.velmaraimaging.net
        <svg class="contact-icon" viewBox="0 0 16 16"><circle cx="8" cy="8" r="7"/></svg>
      </li>
    </ul>

    <div class="address">5873 Calloway ridge ln<br>Raleigh, NC 27614</div>
  </article>
</body>
</html>
```